Cloud Software Services Business Card Design Challenge

We are seeking a fresh and creative business card design that aligns with the brand identity of a startup cloud software services company. As a company specializing in advanced cloud solutions, we want these business cards to reflect our technological leadership and professionalism, helping us stand out in business communications and emphasize our core values.

About Us: We are dedicated to supporting the digital transformation of interior design companies through efficient, reliable, and innovative cloud software services. Our goal is to provide the best technological solutions to drive continuous growth and success for our clients.

Design Requirements:

• Colors: We have not yet established a final color scheme, so please do not feel constrained by the current logo colors. The logo colors can be adjusted according to the overall design. We would like you to choose colors based on your design concept, considering a minimalist, professional, and high-end palette. While many tech companies use a lot of blue, we prefer to avoid this common approach, so feel free to explore other color options.

• Style: The business card design should be modern, clean, and professional, reflecting our technological leadership and innovation capabilities. The design should have a strong visual impact and showcase our expertise in cloud technology.

• Visual Elements: We want the overall feel to be simple and clean. Consider incorporating technology-inspired design elements, such as sleek lines or geometric shapes, to enhance our brand's modern tech image.

• Final Design: The business card should have clear readability and a logical layout, and be suitable for various physical media. The design should accurately reflect our company's professional image and innovative capabilities in the cloud software services field.

• Information Layout: The card should include the following details (we will provide the details for 1 name after selecting the winner and ask the designer to provide four final information of the same design—
1. Chinese version with the job title
2. Chinese version without the job title
3. English version with the job title
4. English version without the job title
o Name
o Job Title
o Company Name and Address
o Tax ID Number
o Phone Number
o Email Address
o Company Website URL
o QR Code

We look forward to seeing how your design can showcase our excellence and professionalism in the cloud software services industry. We hope your creativity will help us effectively communicate our brand values!

Target Market(s)

Interior Design Companies

Contact Information for Business Card

The card should include the following details (we will provide the details for 1 name after selecting the winner and ask the designer to provide four final information of the same design— 1. Chinese version with the job title 2. Chinese version without the job title 3. English version with the job title 4. English version without the job title o Name o Job Title o Company Name and Address o Tax ID Number o Phone Number o Email Address o Company Website URL o QR Code

Colors
0054AA
0677BA
7BADD7
CADEEF
E8F1F8
0094D4
00A9DD
6FCCEA
C7EBF8
E9F6FB
00AB8E
00BBA5
67D7C9
C6EFE9
E9F9F6
FFC000
F8CF3A
FAE287
FDF2CF
FEFAEE
F0912C
F2A743
F7CA91
FBE8D2
FDF5EE
EE7325
F08F49
F5BC92
FAE3D3
FDF4ED
A7469A
B969AE
D3A5CF
EDDBEB
F8F0F9
6B429C
8869AF
B7A5CE
E3DAEB
F3F0F8

```html
<!DOCTYPE html>
<html lang="en">
<head>
<meta charset="utf-8">
<title>Nimbus Loft Business Card</title>
<link href="https://fonts.googleapis.com/css2?family=Lato:wght@400;700;900&family=Noto+Sans+TC:wght@700&display=swap" rel="stylesheet">
<style>
  :root {
    --stage: #1a1a1c;
    --card: #1f1f21;
    --card-edge: #d8ccb0;
    --champagne: #e2d6ba;
    --ink-light: #ebe6dc;
    --ink-soft: #c9c3b8;
    --shade-light: #5a5a5c;
    --shade-dark: #141415;
  }
  * { margin: 0; padding: 0; box-sizing: border-box; }
  html, body {
    width: 1200px; height: 718px; overflow: hidden;
    background: var(--stage);
    font-family: "Lato", sans-serif;
  }
  .stage {
    width: 1200px; height: 718px;
    display: flex; align-items: center; justify-content: center; gap: 40px;
  }
  .card {
    position: relative;
    width: 540px; height: 309px;
    background: var(--card);
    border: 2px solid var(--card-edge);
    border-radius: 18px;
    overflow: hidden;
  }
  /* front */
  .brand-block {
    position: absolute; left: 42px; top: 40px;
    display: flex; flex-direction: column; align-items: center;
  }
  .brand-mark {
    display: flex; align-items: center; gap: 8px;
    font-weight: 900; font-size: 18px; color: var(--champagne); letter-spacing: 0.04em;
    margin-bottom: 10px;
  }
  .brand-dot { width: 9px; height: 9px; border-radius: 50%; background: var(--champagne); }
  .brand-name-zh {
    font-family: "Noto Sans TC", sans-serif; font-weight: 700;
    font-size: 22px; color: #ffffff; letter-spacing: 0.12em;
  }
  .brand-name-en {
    font-size: 10px; color: var(--ink-light); letter-spacing: 0.36em; margin-top: 6px;
  }
  .person {
    position: absolute; right: 40px; top: 44px; text-align: right;
  }
  .person-name { font-weight: 900; font-size: 22px; color: var(--champagne); letter-spacing: 0.02em; }
  .person-title { font-size: 12px; color: var(--ink-light); margin-top: 2px; }
  .contact {
    position: absolute; left: 42px; bottom: 30px;
    color: var(--ink-light); font-size: 12px; line-height: 1.45;
  }
  .contact-company { font-weight: 700; color: var(--champagne); font-size: 12.5px; }
  .contact-address { margin-bottom: 8px; }
  .contact-row { display: flex; align-items: center; gap: 8px; }
  .contact-row svg { width: 12px; height: 12px; flex: none; }
  .feature-art {
    position: absolute; right: 0; bottom: 0; width: 270px; height: 200px;
    background: linear-gradient(135deg, var(--shade-light) 0%, #2c2c2e 45%, var(--shade-dark) 100%);
    border-top-left-radius: 100px;
  }
  /* back */
  .pattern-field {
    position: absolute; inset: 0;
    background: linear-gradient(100deg, #8a8a8c 0%, #3a3a3c 35%, #141415 75%, #0d0d0e 100%);
    opacity: 0.55;
  }
  .back-mark {
    position: absolute; right: 34px; bottom: 70px;
    display: flex; align-items: center; gap: 8px;
    font-weight: 900; font-size: 16px; color: var(--champagne); letter-spacing: 0.04em;
  }
  .back-mark .brand-dot { width: 8px; height: 8px; }
</style>
</head>
<body>
<main class="stage">
  <section class="card card-front">
    <div class="brand-block">
      <div class="brand-mark"><span class="brand-dot"></span>NIMBUS LOFT</div>
      <div class="brand-name-zh">雲栩科技股份有限公司</div>
      <div class="brand-name-en">NIMBUS LOFT</div>
    </div>
    <div class="person">
      <div class="person-name">DANIEL REYES</div>
      <div class="person-title">Founder &amp; CEO</div>
    </div>
    <div class="feature-art" role="img" aria-label="Large grey geometric brand graphic with a circle and folded peaks"></div>
    <div class="contact">
      <div class="contact-company">Nimbus Loft Group</div>
      <div class="contact-address">88 Harbor Lane Suite 5, City<br>State &amp; Country, ZIP Code</div>
      <div class="contact-row">
        <svg viewBox="0 0 12 12" fill="none" stroke="var(--ink-light)" stroke-width="1"><rect x="1.5" y="1.5" width="9" height="9" rx="1"/><line x1="3.5" y1="4.5" x2="8.5" y2="4.5"/><line x1="3.5" y1="7" x2="8.5" y2="7"/></svg>
        <span>(555) 010-2040</span>
      </div>
      <div class="contact-row">
        <svg viewBox="0 0 12 12" fill="var(--ink-light)"><path d="M2.5 1h2l1 2.5-1.3 1a6 6 0 0 0 3.3 3.3l1-1.3L11 7.5v2A1.5 1.5 0 0 1 9.5 11C5 11 1 7 1 2.5A1.5 1.5 0 0 1 2.5 1z"/></svg>
        <span>(555) 010-2040</span>
      </div>
      <div class="contact-row">
        <svg viewBox="0 0 12 12" fill="none" stroke="var(--ink-light)" stroke-width="1"><rect x="1" y="2.5" width="10" height="7" rx="0.8"/><polyline points="1,3 6,7 11,3"/></svg>
        <span>info@nimbusloft.com</span>
      </div>
      <div class="contact-row">
        <svg viewBox="0 0 12 12" fill="none" stroke="var(--ink-light)" stroke-width="1"><circle cx="6" cy="6" r="5"/><ellipse cx="6" cy="6" rx="2.2" ry="5"/><line x1="1" y1="6" x2="11" y2="6"/></svg>
        <span>nimbusloft.com</span>
      </div>
    </div>
  </section>

  <section class="card card-back">
    <div class="pattern-field" role="img" aria-label="Repeating glossy brand pattern fading from light grey to black"></div>
    <div class="back-mark"><span class="brand-dot"></span>NIMBUS LOFT</div>
  </section>
</main>
</body>
</html>
```